Create a Landing Page Design

I need a landing page designed and coded in HTML for tallfern.com that follows an "F" pattern design.

Examples:

Quillbarrow: https://www.quillbarrow.example/form/sem/sales_software.jsp?d=48260000000tkP7&DCMP=KNC-Search&mkwid=R8wq2Lm5&pcrid=58204917362&type=Exact&pdv=c&nc=48260000000mbHQ&gclid=DKoRn47f2M1DGfSmPhpeRHxBkR
Jug: https://app.jug.example/signup/o/sendlargefiles?kw=jug%20cloud%20storage&gclid=DJaLrfnf2M1DGT2fPhpe1GNBOR
Cobaltwick: http://www.cobaltwick.example/Landing-Templates/Search-Demo/?Reach_Campaign_ID=48270000000Jtwu&Reach_Campaign_Status=Registered&LeadSource=OnlineDemo_Search_48270000000Jtwu&PromoCode=OnlineDemo_Search_48270000000Jtwu&gclid=DJD1pL7g2M1DGZziPhpePH5B6R
Plumtide: http://pages2.plumtide.example/PPC-MarketingAutomationforLife.html?source=PPC&comment=PPC_GS_US&ag=Competition%20-%20Norvane&camp=Competition%20Marketing%20Automation&_kk=52542849458&kw=norvane&gclid=DMzSmKPg2M1DGX6fPhpeQycBLB
Gladwell Helper: http://gladwellhelper.example/free-helpdesk-software?gclid=DKQFovjg2M1DGfxEPhpegNB1h
Pult: http://help.pult.example/free-trial?source1=Adverts-CPC-Freetrial-BramlineNA&pi_ad_id=59602686359&gclid=DQ_ftf3g2M1DGf18PhpeilJBvB

It needs:

- Bullet point content to the left
- Sign-up form to the right (with image) - we'll provide the code for this
- Testimonials underneath
- A "human" image that conveys that there are people behind the brand. Here's a link to a filecrate folder of stock images we've purchased on this theme: https://www.filecrate.example/sh/uz1fbp5upmj0nvy/q5hL7VVvl8

I've attached a simple SketchRill wireframe so you understand what we're looking for.

We'd like to use our existing (https://tallfern.com/) header and footer, but remove all links (other than privacy policy + terms of service).

Thanks!

```html
<!DOCTYPE html>
<html lang="en">
<head>
<meta charset="utf-8">
<title>Tallfern – Freelance Talent</title>
<link href="https://fonts.googleapis.com/css2?family=Arimo:ital,wght@0,400;0,700;1,400&display=swap" rel="stylesheet">
<style>
  :root{
    --ink:#444;
    --muted:#777;
    --brand-blue:#1a7fb5;
    --link-blue:#1682b8;
    --cta:#33b2d8;
    --cta-edge:#1f8fb4;
    --line:#dcdcdc;
    --field-bg:#f4f4f4;
    --field-border:#c9c9c9;
    --band:#e5e5e5;
    --footer:#2b2b2b;
    --topbar:#222;
  }
  *{box-sizing:border-box;margin:0;padding:0}
  html,body{width:1200px;height:1161px;overflow:hidden;background:#fff}
  body{position:relative;font-family:"Arimo",Arial,sans-serif;color:var(--ink)}
  .abs{position:absolute}

  .top-bar{left:0;top:0;width:1200px;height:6px;background:var(--topbar)}
  .header-rule{left:0;top:98px;width:1200px;height:3px;background:var(--brand-blue)}
  .brand{display:flex;align-items:center;gap:12px}
  .brand-dot{border-radius:50%;background:var(--brand-blue)}
  .brand-name{color:var(--muted);font-weight:400}
  .header-brand{left:178px;top:28px}
  .header-brand .brand-dot{width:54px;height:54px}
  .header-brand .brand-name{font-size:43px}

  .intro-frame{left:171px;top:155px;width:277px;height:115px;border:1px solid var(--line);padding:5px;background:#fff}
  .intro-frame-inner{width:100%;height:100%;background:#f5f5f5;display:flex;align-items:center;justify-content:center}
  .intro-frame .brand-dot{width:30px;height:30px}
  .intro-frame .brand-name{font-size:22px}
  .intro-copy{left:471px;top:160px;width:560px}
  .intro-title{color:var(--link-blue);font-size:14.6px;line-height:20.5px;font-weight:400;margin-bottom:6px}
  .intro-text{font-size:10.4px;line-height:20.5px;color:var(--ink)}

  .divider{left:171px;top:310px;width:858px;height:10px;background:radial-gradient(ellipse at 50% 0,rgba(0,0,0,.12),rgba(0,0,0,0) 70%)}

  .features{left:171px;top:368px;width:463px}
  .feature{position:relative;height:116px;border-bottom:1px solid var(--line);background:linear-gradient(#fff 70%,#f2f2f2)}
  .feature-icon{position:absolute;left:13px;top:4px;width:64px;height:64px;border-radius:12px}
  .feature h3{position:absolute;left:92px;top:10px;font-size:14px;font-weight:400;color:var(--link-blue)}
  .feature p{position:absolute;left:92px;top:35px;width:360px;font-size:10.4px;line-height:20.5px}
  .icon-person{background:radial-gradient(circle at 50% 40%,#e8b88a,#2e5c9a 70%)}
  .icon-books{background:linear-gradient(90deg,#2f5c3a,#7a2a22,#2a3f7a,#9a5a2a)}
  .icon-chart{border-radius:50%;background:conic-gradient(#f2c01a 0 65%,#7cc04a 65% 85%,#3aa0d8 85%)}
  .icon-tools{background:linear-gradient(135deg,#c9cdd2,#d62e2e 50%,#2a5cc0)}

  .signup{left:657px;top:360px;width:372px;height:463px;border:1px solid #dedede;overflow:hidden}
  .signup-photo{position:absolute;inset:0;background:radial-gradient(ellipse at 45% 35%,#f3e7de 0,#eef0f3 45%,#f1f3f6 100%)}
  .signup-form{position:absolute;inset:0}
  .field{position:absolute;left:0;width:372px;height:28px}
  .field label{position:absolute;right:252px;top:7px;font-size:10.4px;color:#555;white-space:nowrap}
  .field input,.field .select{position:absolute;left:132px;top:0;width:214px;height:28px;background:var(--field-bg);border:1px solid var(--field-border);font-family:inherit;font-size:10.4px;color:#777;padding-left:9px;line-height:26px}
  .cta{position:absolute;left:132px;top:368px;width:214px;height:43px;background:var(--cta);border:0;border-bottom:3px solid var(--cta-edge);color:#fff;font-family:inherit;font-size:14.6px;letter-spacing:.2px}
  .terms{position:absolute;right:26px;top:427px;font-size:10.4px;color:#777}

  .testimonials{left:0;top:864px;width:1200px;height:210px;background:var(--band)}
  .t-heading{left:171px;top:24px;font-size:17px;font-weight:400;color:var(--link-blue)}
  .t-arrows{left:1007px;top:28px;display:flex;gap:6px}
  .quote{top:70px;width:430px;height:105px}
  .quote-photo{position:absolute;left:3px;top:0;width:102px;height:102px;border-radius:50%;border:3px solid #fff}
  .photo-a{background:linear-gradient(#e9e4dd 0 30%,#c99a78 30% 60%,#7fa8d8 60%)}
  .photo-b{background:linear-gradient(#ece8e4 0 30%,#b48a6e 30% 60%,#222 60%)}
  .quote-name{position:absolute;left:131px;top:18px;font-size:14px;font-weight:400;color:var(--link-blue)}
  .quote-date{position:absolute;left:131px;top:41px;font-size:10.4px;font-style:italic;color:#333}
  .quote-text{position:absolute;left:130px;top:66px;width:280px;font-size:10.4px;line-height:20.5px}
  .partner{position:absolute;left:298px;top:10px;width:102px;height:42px;background:#fff;border:1px solid #ccc;display:flex;align-items:center;justify-content:center;font-size:13px;color:#555}

  .footer{left:0;top:1074px;width:1200px;height:87px;background:var(--footer)}
  .copyright{left:190px;top:39px;font-size:10.4px;color:#666}
  .copyright a{color:#666}
  .footer-brand{left:795px;top:26px}
  .footer-brand .brand-dot{width:30px;height:30px;background:#f08a1c}
  .footer-brand .brand-name{font-size:25px;color:#8a8a8a}
</style>
</head>
<body>
  <div class="abs top-bar"></div>
  <header>
    <div class="abs brand header-brand"><span class="brand-dot"></span><span class="brand-name">Tallfern</span></div>
    <div class="abs header-rule"></div>
  </header>

  <section>
    <div class="abs intro-frame"><div class="intro-frame-inner"><div class="brand"><span class="brand-dot"></span><span class="brand-name">Tallfern</span></div></div></div>
    <div class="abs intro-copy">
      <h1 class="intro-title">We aggregate the top freelance platforms to bring you the world’s largest and most diverse pool of freelance workers.</h1>
      <p class="intro-text">We aggregate the top freelance platforms to bring you the world’s largest and most diverse pool of freelance workersWe aggregate the top freelance platforms to bring you the world’s largest and most diverse pool of freelance workersWe aggregate the top freelance platforms to bring you the world’s largest and most diverse pool of freelance workers.</p>
    </div>
    <div class="abs divider"></div>
  </section>

  <section class="abs features">
    <div class="feature"><div class="feature-icon icon-person" role="img" aria-label="Illustration of a businessman"></div><h3>More Talent Than You Will Ever Need!</h3><p>We aggregate the top freelance platforms to bring you the world’s largest and most diverse pool of freelance workers.</p></div>
    <div class="feature"><div class="feature-icon icon-books" role="img" aria-label="Illustration of books on a stand"></div><h3>More Talent Than You Will Ever Need!</h3><p>We aggregate the top freelance platforms to bring you the world’s largest and most diverse pool of freelance workers.</p></div>
    <div class="feature"><div class="feature-icon icon-chart" role="img" aria-label="Illustration of a pie chart"></div><h3>More Talent Than You Will Ever Need!</h3><p>We aggregate the top freelance platforms to bring you the world’s largest and most diverse pool of freelance workers.</p></div>
    <div class="feature"><div class="feature-icon icon-tools" role="img" aria-label="Illustration of a wrench and screwdriver"></div><h3>More Talent Than You Will Ever Need!</h3><p>We aggregate the top freelance platforms to bring you the world’s largest and most diverse pool of freelance workers.</p></div>
  </section>

  <section class="abs signup">
    <div class="signup-photo" role="img" aria-label="Faded photo of a smiling woman in glasses"></div>
    <form class="signup-form">
      <div class="field" style="top:28px"><label>First name :</label><input type="text"></div>
      <div class="field" style="top:71px"><label>Last name :</label><input type="text"></div>
      <div class="field" style="top:114px"><label>Email :</label><input type="text"></div>
      <div class="field" style="top:157px"><label>Password :</label><input type="password"></div>
      <div class="field" style="top:200px"><label>Conform Password :</label><input type="password"></div>
      <div class="field" style="top:243px"><label>Your Phone :</label><input type="text"></div>
      <div class="field" style="top:285px"><label>Business Name :</label><div class="select">Please select an option</div></div>
      <div class="field" style="top:328px"><label>Zop Code :</label><input type="text"></div>
      <button type="button" class="cta">GET STARTED</button>
      <p class="terms">By registering you agree to Jug's Trial Terms of Service</p>
    </form>
  </section>

  <section class="abs testimonials">
    <h2 class="abs t-heading">Testimonials</h2>
    <div class="abs t-arrows">
      <svg width="8" height="10" viewBox="0 0 8 10"><path d="M6 1 2 5l4 4" fill="none" stroke="#999" stroke-width="1.3"/></svg>
      <svg width="8" height="10" viewBox="0 0 8 10"><path d="M2 1l4 4-4 4" fill="none" stroke="#999" stroke-width="1.3"/></svg>
    </div>
    <article class="abs quote" style="left:171px">
      <div class="quote-photo photo-a" role="img" aria-label="Portrait photo of a smiling man in glasses"></div>
      <h3 class="quote-name">Marlo Quint</h3>
      <p class="quote-date">Thursday 22 November</p>
      <div class="partner">Kettlewing</div>
      <p class="quote-text">We aggregate the top freelance platforms to bring you the world's largest and most diverse pool...</p>
    </article>
    <article class="abs quote" style="left:628px">
      <div class="quote-photo photo-b" role="img" aria-label="Portrait photo of a businesswoman"></div>
      <h3 class="quote-name">Marlo Quint</h3>
      <p class="quote-date">Thursday 22 November</p>
      <div class="partner">Ledgerpane</div>
      <p class="quote-text">We aggregate the top freelance platforms to bring you the world's largest and most diverse pool...</p>
    </article>
  </section>

  <footer class="abs footer">
    <p class="abs copyright">Copyright © 2014 Tallfern, Inc. Eastbrook, OR | All Rights Reserved | <a href="#">Terms and Conditions</a> | <a href="#">Privacy Policy</a></p>
    <div class="abs brand footer-brand"><span class="brand-dot"></span><span class="brand-name">Tallfern</span></div>
  </footer>
</body>
</html>
```